Design my dad a new business card because his current one sucks!

I need a business card designed for my fathers home maintenance business. His customers are individuals (single moms, old people etc.) as well as the occasional business. As such it needs to be accessible to both target audiences.

The front of the card should be dark grey on yellow with the logo and contain the following information:
- Warren Dobrinski
- 0487 362 914
- info@harbourlinehandyworks.com.au
- 0487 362 914

- ABN: 87 214 630 592
- 'Fully Insured'

The reverse should be yellow on dark grey and will have the web address:
- harbourlinehandyworks.com.au

And a few key services he offers:
GENERAL REPAIRS
PAINTING/TILING/
PAVING &CONCRETING
PRESSURE WASHING
ON-SITE WELDING
DECKING ADDITIONS & REPAIRS
FENCING
FULL BOND CLEANING

This will be first time the logo has been printed so you will need to come up with the best CMYK approximation of the RGB colours to make sure it is a close as possible.

```html
<!DOCTYPE html>
<html lang="en">
<head>
<meta charset="utf-8">
<title>Harbourline Handyworks – Business Card</title>
<link rel="stylesheet" href="https://fonts.googleapis.com/css2?family=Play:wght@400;700&display=swap">
<style>
  :root {
    --backdrop: #a4a4a4;
    --yellow: #f6c21c;
    --ink: #333333;
    --ink-soft: #3a3a3a;
  }
  * { margin: 0; padding: 0; box-sizing: border-box; }
  html, body { width: 1200px; height: 894px; overflow: hidden; }
  body {
    background: var(--backdrop);
    font-family: "Play", sans-serif;
    color: var(--ink);
    position: relative;
  }
  .card {
    position: absolute;
    width: 540px;
    height: 308px;
    top: 293px;
    box-shadow: 0 6px 18px rgba(0,0,0,0.18);
    overflow: hidden;
  }
  .card--front { left: 40px; background: var(--yellow); color: var(--ink); }
  .card--back { left: 620px; background: var(--ink); color: var(--yellow); }

  .wordmark { position: absolute; line-height: 1; font-weight: 700; }
  .wordmark__name { display: block; letter-spacing: -1px; }
  .wordmark__tag { display: block; letter-spacing: 2px; }

  .card--front .wordmark { left: 28px; top: 22px; }
  .card--front .wordmark__name { font-size: 46px; }
  .card--front .wordmark__tag { font-size: 13px; margin-top: 4px; padding-left: 64px; }

  .card--back .wordmark { left: 0; right: 0; top: 28px; text-align: center; }
  .card--back .wordmark__name { font-size: 46px; }
  .card--back .wordmark__tag { font-size: 13px; margin-top: 4px; padding-left: 90px; }

  .band { position: absolute; top: 118px; height: 40px; background: var(--ink); }
  .band--short { left: 0; width: 168px; clip-path: polygon(0 0, 100% 0, calc(100% - 6px) 100%, 0 100%); }
  .band--long {
    left: 176px; right: 0;
    clip-path: polygon(6px 0, 100% 0, 100% 100%, 0 100%);
    display: flex; align-items: center;
    padding-left: 40px;
  }
  .band__web { color: var(--yellow); font-size: 13px; letter-spacing: 1px; }

  .person { position: absolute; right: 30px; top: 68px; }
  .person__name { font-size: 17px; font-weight: 700; letter-spacing: 1px; text-transform: uppercase; }
  .person__role { font-size: 11px; letter-spacing: 1px; text-transform: uppercase; }

  .contact-list { position: absolute; list-style: none; }
  .contact-list--details { left: 28px; top: 174px; }
  .contact-list--links { left: 300px; top: 226px; }
  .contact-list li { display: flex; align-items: center; gap: 8px; font-size: 10.5px; height: 20px; color: var(--ink-soft); }
  .contact-list .contact-list__note { font-weight: 700; letter-spacing: 1px; text-transform: uppercase; padding-left: 22px; }
  .contact-icon { width: 14px; height: 14px; flex: none; display: block; }

  .services {
    position: absolute; left: 50px; right: 30px; top: 124px;
    list-style: none;
    display: grid; grid-template-columns: 1fr 1fr; grid-auto-rows: 22px;
    font-size: 11px; font-weight: 700; letter-spacing: 1px;
  }
  .services li { display: flex; align-items: center; gap: 8px; }
  .services li::before { content: ""; width: 6px; height: 6px; background: var(--yellow); flex: none; }
  .back-web {
    position: absolute; left: 0; right: 0; bottom: 0; height: 40px;
    background: var(--yellow); color: var(--ink);
    display: flex; align-items: center; justify-content: center;
    font-size: 13px; letter-spacing: 1px;
  }
</style>
</head>
<body>

<section class="card card--front" aria-label="Business card front">
  <div class="wordmark">
    <span class="wordmark__name">Harbourline</span>
    <span class="wordmark__tag">HANDYWORKS</span>
  </div>

  <div class="person">
    <p class="person__name">Warren Dobrinski</p>
    <p class="person__role">Manager</p>
  </div>

  <div class="band band--short"></div>
  <div class="band band--long"><span class="band__web">www.harbourlinehandyworks.com.au</span></div>

  <ul class="contact-list contact-list--details">
    <li>
      <svg class="contact-icon" viewBox="0 0 14 14" aria-hidden="true"><rect width="14" height="14" fill="#333"/><path d="M7 3a2.5 2.5 0 0 0-2.5 2.5C4.5 7.5 7 11 7 11s2.5-3.5 2.5-5.5A2.5 2.5 0 0 0 7 3z" fill="#f6c21c"/><circle cx="7" cy="5.5" r="0.9" fill="#333"/></svg>
      <span>14 Wharf Lane 2000</span>
    </li>
    <li>
      <svg class="contact-icon" viewBox="0 0 14 14" aria-hidden="true"><rect width="14" height="14" fill="#333"/><path d="M4.2 3.2l1.6-.2.8 2-1 .8a5 5 0 0 0 2.6 2.6l.8-1 2 .8-.2 1.6c-3.6.4-7-3-6.6-6.6z" fill="#f6c21c"/></svg>
      <span>0487 362 914</span>
    </li>
    <li>
      <svg class="contact-icon" viewBox="0 0 14 14" aria-hidden="true"><rect width="14" height="14" fill="#333"/><rect x="3" y="4.2" width="8" height="5.6" fill="#f6c21c"/><path d="M3 4.2l4 3 4-3" stroke="#333" stroke-width="0.8" fill="none"/></svg>
      <span>info@harbourlinehandyworks.com.au</span>
    </li>
    <li class="contact-list__note">ABN: 87 214 630 592</li>
    <li class="contact-list__note">Fully Insured</li>
  </ul>

  <ul class="contact-list contact-list--links">
    <li>
      <svg class="contact-icon" viewBox="0 0 14 14" aria-hidden="true"><rect width="14" height="14" fill="#333"/></svg>
      <span>www.harbourlinehandyworks.com.au</span>
    </li>
    <li>
      <svg class="contact-icon" viewBox="0 0 14 14" aria-hidden="true"><rect width="14" height="14" fill="#333"/></svg>
      <span>www.chirpwire.net</span>
    </li>
    <li>
      <svg class="contact-icon" viewBox="0 0 14 14" aria-hidden="true"><rect width="14" height="14" fill="#333"/></svg>
      <span>www.neighbourpage.net</span>
    </li>
  </ul>
</section>

<section class="card card--back" aria-label="Business card back">
  <div class="wordmark">
    <span class="wordmark__name">Harbourline</span>
    <span class="wordmark__tag">HANDYWORKS</span>
  </div>

  <ul class="services">
    <li>GENERAL REPAIRS</li>
    <li>PRESSURE WASHING</li>
    <li>PAINTING / TILING</li>
    <li>ON-SITE WELDING</li>
    <li>PAVING &amp; CONCRETING</li>
    <li>DECKING ADDITIONS &amp; REPAIRS</li>
    <li>FENCING</li>
    <li>FULL BOND CLEANING</li>
  </ul>

  <div class="back-web">harbourlinehandyworks.com.au</div>
</section>

</body>
</html>
```